Kestrel Schools Vinyl Banner

Based on the attached images design a image that we will be printed onto a vinyl Banner and used at conventions.

Design liberties are welcome but it needs to look good and the the final submission will need to be submitted in .psd format with all layers being able to be edited.

Make it look good and atract new business

```html
<!DOCTYPE html>
<html lang="en">
<head>
<meta charset="utf-8">
<title>Kestrel Schools – Welcome Graduates Banner</title>
<link href="https://fonts.googleapis.com/css2?family=Bebas+Neue&family=Open+Sans:wght@700&display=swap" rel="stylesheet">
<style>
  :root {
    --stage: #242424;
    --banner: #ffffff;
    --navy: #1b355e;
    --accent-mist: #b3c7cf;
    --accent-blue: #1b6aa0;
    --accent-teal: #23797a;
  }
  html, body {
    margin: 0;
    width: 1200px;
    height: 1200px;
    overflow: hidden;
    background: var(--stage);
  }
  .banner {
    position: absolute;
    left: 53px;
    top: 381px;
    width: 1094px;
    height: 437px;
    background: var(--banner);
    overflow: hidden;
  }
  .banner__accent {
    position: absolute;
    top: 0;
    right: 0;
    width: 180px;
    height: 437px;
    background: linear-gradient(160deg, var(--accent-mist) 0%, var(--accent-blue) 55%, var(--accent-teal) 100%);
  }
  .banner__headline {
    position: absolute;
    left: 28px;
    top: 38px;
    margin: 0;
    font-family: "Bebas Neue", sans-serif;
    font-weight: 400;
    font-size: 116px;
    line-height: 1;
    letter-spacing: 4px;
    color: var(--navy);
    white-space: nowrap;
  }
  .brand {
    position: absolute;
    left: 41px;
    top: 195px;
    display: flex;
    align-items: center;
    gap: 44px;
  }
  .brand__dot {
    width: 104px;
    height: 104px;
    border-radius: 50%;
    background: var(--navy);
  }
  .brand__name {
    font-family: "Bebas Neue", sans-serif;
    font-weight: 400;
    font-size: 64px;
    line-height: 0.82;
    letter-spacing: 6px;
    color: var(--navy);
  }
  .banner__url {
    position: absolute;
    left: 41px;
    top: 372px;
    margin: 0;
    font-family: "Open Sans", sans-serif;
    font-weight: 700;
    font-size: 18px;
    letter-spacing: 4.2px;
    color: var(--navy);
  }
</style>
</head>
<body>
  <section class="banner">
    <div class="banner__accent" role="img" aria-label="Decorative flowing ribbon in grey, blue and teal"></div>

    <h1 class="banner__headline">Welcome Graduates</h1>

    <div class="brand">
      <span class="brand__dot"></span>
      <span class="brand__name">Kestrel<br>Schools</span>
    </div>

    <p class="banner__url">www.kestrelschools.com.au</p>
  </section>
</body>
</html>
```